GIFT BOX FOR DECORATION CHRISTMAS

Good evening, the job to do is to create a gift box with the attached path.
The Gift Box is for a company that deals with personalized Christmas decorations.
The graphics must be "very clean", the colors to be used are RED and GREEN the colors of Christmas. In the graphics we put a beautiful bow and the company logo.
I am attaching the company's logo to some examples.

good job

Target Market(s)

Being a Gift Box for a Christmas product must be suitable for everyone.

Font styles to use
Sans Serif

Colors
00a990
ec1f27

Requirements
Must have
• The project must have a background (green / red) a bow, inside the logo must be placed. In the sides of the Gift, reverse the color (as per the sample from last year attached) insert the PALWIRE logo and PIXORVA + WEB SITE (www.casaluminara.it)

```html
<!DOCTYPE html>
<html lang="it">
<head>
<meta charset="utf-8">
<title>Casa Luminara – Gift Box Dieline</title>
<link rel="stylesheet" href="https://fonts.googleapis.com/css2?family=Open+Sans:ital,wght@0,400;0,600;0,700;1,600&display=swap">
<style>
  :root{
    --green:#00a990;
    --green-line:#0a7d6b;
    --green-deep:#0b5a4c;
    --red:#ec1f27;
    --red-dark:#d81820;
    --red-pale:#f7b3b5;
    --white:#ffffff;
    --label-grey:#eeeeee;
    --page:#ffffff;
  }
  html,body{margin:0;padding:0;overflow:hidden;background:var(--page);}
  .canvas{width:1200px;height:800px;display:block;}
  .panel{fill:url(#greenField);stroke:var(--green-line);stroke-width:1;}
  .fold{stroke:var(--green-line);stroke-width:1;fill:none;}
  .cut-white{fill:var(--white);stroke:var(--green-line);stroke-width:1;}
  .pattern-area{fill:url(#festivePattern);}
  .pattern-strip{fill:url(#paleStrip);}
  .front-band{fill:url(#redBand);}
  .label-outer{fill:var(--white);}
  .label-inner{fill:var(--label-grey);}
  .bow{fill:url(#bowTone);}
  .wreath{fill:url(#wreathTone);}
  .ornament{fill:url(#flourishTone);}
  .brand-name{font-family:"Open Sans",sans-serif;font-weight:700;fill:var(--red);}
  .tagline{font-family:"Open Sans",sans-serif;font-weight:600;font-style:italic;fill:#333;}
  .web{font-family:"Open Sans",sans-serif;font-weight:700;fill:var(--white);}
  .follow{font-family:"Open Sans",sans-serif;font-weight:600;fill:var(--white);}
  .social-dot{fill:var(--green-deep);}
  .social-name{font-family:"Open Sans",sans-serif;font-weight:700;fill:var(--white);}
</style>
</head>
<body>
<svg class="canvas" viewBox="0 0 1500 1000" xmlns="http://www.w3.org/2000/svg">
  <defs>
    <linearGradient id="greenField" x1="0" y1="0" x2="0" y2="1">
      <stop offset="0" stop-color="#03ad94"/>
      <stop offset="1" stop-color="#00a48b"/>
    </linearGradient>
    <linearGradient id="festivePattern" x1="0" y1="0" x2="1" y2="1">
      <stop offset="0" stop-color="#ee3a40"/>
      <stop offset=".3" stop-color="#f26a6f"/>
      <stop offset=".55" stop-color="#ec2a31"/>
      <stop offset=".8" stop-color="#f2686d"/>
      <stop offset="1" stop-color="#ec262d"/>
    </linearGradient>
    <linearGradient id="paleStrip" x1="0" y1="0" x2="1" y2="0">
      <stop offset="0" stop-color="#f9c9ca"/>
      <stop offset=".5" stop-color="#fbdcdc"/>
      <stop offset="1" stop-color="#f7b3b5"/>
    </linearGradient>
    <linearGradient id="redBand" x1="0" y1="0" x2="1" y2="1">
      <stop offset="0" stop-color="#e81e26"/>
      <stop offset="1" stop-color="#d8171f"/>
    </linearGradient>
    <radialGradient id="bowTone" cx=".5" cy=".45" r=".5">
      <stop offset="0" stop-color="#e8363c"/>
      <stop offset=".7" stop-color="#c4161e"/>
      <stop offset="1" stop-color="#c4161e" stop-opacity="0"/>
    </radialGradient>
    <radialGradient id="wreathTone" cx=".5" cy=".5" r=".5">
      <stop offset="0" stop-color="#f3d7c8"/>
      <stop offset=".35" stop-color="#e0474a"/>
      <stop offset=".6" stop-color="#2f7a3a"/>
      <stop offset=".95" stop-color="#1f5e2a"/>
      <stop offset="1" stop-color="#1f5e2a" stop-opacity="0"/>
    </radialGradient>
    <radialGradient id="flourishTone" cx=".5" cy=".5" r=".5">
      <stop offset="0" stop-color="#0b5a4c" stop-opacity=".7"/>
      <stop offset="1" stop-color="#0b5a4c" stop-opacity="0"/>
    </radialGradient>
  </defs>

  <g class="front">
    <path class="panel" d="M193 97 V45 Q193 25 213 25 H448 Q468 25 468 45 V97 Z"/>
    <path class="fold" d="M272 97 V93 H362 V97"/>
    <rect class="panel" x="77" y="97" width="508" height="711"/>
    <rect class="cut-white" x="173" y="185" width="316" height="20" rx="10"/>
    <path class="panel" d="M77 293 L18 330 V748 L77 808 Z"/>
    <path class="panel" d="M77 808 H585 L578 828 V964 H560 L490 908 H330 L265 964 H90 Z"/>

    <rect class="pattern-area" x="77" y="293" width="508" height="310" role="img" aria-label="Christmas pattern of reindeer, trees and baubles in pale red on red"/>
    <rect class="pattern-strip" x="77" y="603" width="508" height="37" role="img" aria-label="Pale pink diamond pattern strip"/>
    <rect class="front-band" x="77" y="640" width="508" height="168" role="img" aria-label="Red band with fine diagonal stripes"/>

    <rect class="label-outer" x="158" y="448" width="356" height="252" rx="70"/>
    <rect class="label-inner" x="185" y="472" width="302" height="204" rx="50"/>

    <ellipse class="bow" cx="360" cy="470" rx="80" ry="85" role="img" aria-label="Red satin ribbon bow"/>

    <text class="brand-name" x="332" y="566" font-size="42" text-anchor="middle">Casa</text>
    <text class="brand-name" x="332" y="612" font-size="42" text-anchor="middle">Luminara</text>
    <text class="tagline" x="438" y="635" font-size="18" text-anchor="end">The Original</text>

    <circle class="wreath" cx="328" cy="703" r="58" role="img" aria-label="Company emblem: holly wreath with red bow"/>

    <text class="web" x="329" y="791" font-size="14" text-anchor="middle">www.casaluminara.it</text>
  </g>

  <g class="side-left">
    <rect class="panel" x="597" y="213" width="172" height="85"/>
    <rect class="panel" x="585" y="298" width="196" height="510"/>
    <path class="panel" d="M585 808 H781 L700 905 H605 Z"/>
    <text class="follow" x="683" y="634" font-size="14" text-anchor="middle">seguici su</text>
    <circle class="social-dot" cx="618" cy="655" r="7"/>
    <text class="social-name" x="629" y="660" font-size="12">PALWIRE</text>
    <circle class="social-dot" cx="692" cy="655" r="7"/>
    <text class="social-name" x="703" y="660" font-size="12">PIXORVA</text>
    <text class="web" x="683" y="686" font-size="14" text-anchor="middle">www.casaluminara.it</text>
    <ellipse class="ornament" cx="685" cy="705" rx="62" ry="11" role="img" aria-label="Decorative flourish"/>
  </g>

  <g class="back">
    <path class="panel" d="M785 105 V48 Q785 28 805 28 H1265 Q1285 28 1285 48 V105 Z"/>
    <rect class="panel" x="781" y="105" width="509" height="703"/>
    <path class="fold" d="M781 298 H900 V290 H1172 V298 H1290"/>
    <circle class="cut-white" cx="905" cy="198" r="9"/>
    <circle class="cut-white" cx="1165" cy="198" r="9"/>
    <path class="cut-white" d="M977 355 V268 Q977 246 999 246 H1071 Q1093 246 1093 268 V355 Z"/>
    <path class="fold" d="M1008 298 A27 27 0 0 0 1062 298"/>
    <path class="panel" d="M781 808 H1290 L1284 828 V964 H1265 L1195 908 H1035 L970 964 H795 Z"/>

    <circle class="wreath" cx="1036" cy="508" r="132" role="img" aria-label="Company emblem: holly wreath with red bow and ribbon banner"/>

    <text class="web" x="1036" y="777" font-size="21" text-anchor="middle">www.casaluminara.it</text>
  </g>

  <g class="side-right">
    <rect class="panel" x="1302" y="213" width="171" height="85"/>
    <rect class="panel" x="1290" y="298" width="191" height="510"/>
    <path class="panel" d="M1290 808 H1481 L1400 905 H1300 Z"/>
    <text class="follow" x="1385" y="625" font-size="14" text-anchor="middle">seguici su</text>
    <circle class="social-dot" cx="1320" cy="646" r="7"/>
    <text class="social-name" x="1331" y="651" font-size="12">PALWIRE</text>
    <circle class="social-dot" cx="1394" cy="646" r="7"/>
    <text class="social-name" x="1405" y="651" font-size="12">PIXORVA</text>
    <text class="web" x="1385" y="677" font-size="14" text-anchor="middle">www.casaluminara.it</text>
    <ellipse class="ornament" cx="1385" cy="696" rx="60" ry="11" role="img" aria-label="Decorative flourish"/>
  </g>
</svg>
</body>
</html>
```